Flyer Design for Private Car Service

Flyer should cater to Business Travelers and Executives who travel Business Class or First Class.
Flyer should include images attached.
Flyer should include the below text
Dallas to Austin
Chauffeured SUVs
• Travel Dallas to Austin in a new 2025 Marlow Strider for $499 one-way
• Trip includes a Uniformed Chauffeur who has a Commercial Drivers License (CDL)
• You can Schedule Chauffeur Pickup at Your Home in Dallas
• Our Chauffeur will Drop You Off at Your Final Destination in Austin
• You can Schedule Chauffeur Return Pickup in Austin and Return Back to Dallas.
• We offer Faster Times on Door-to-Door Travel than Bluecrest Airways
• We offer Comparable Prices on Door-to-Door Travel Times than Bluecrest Airways
• All of our trips are insured with $500k of commercial auto insurance
• Our Passengers can Talk on Cell Phone & Conduct Quill calls Throughout Travel
• Our Passengers have Maximum Privacy, Comfort and First-Class Amenities.
• Our Passengers Avoid Harwick Vale Field and KPR Airport hassles & delays
• Member Brenton Chamber of Commerce, Larkmoor Chamber of Commerce.
• Book your trip today at www.ridemarquel.example
Target Market(s)
Business Travelers
Look and feel
Each slider illustrates characteristics of the customer's brand and the style your logo design should communicate.

```html
<!DOCTYPE html>
<html lang="en">
<head>
<meta charset="utf-8">
<title>Marquel – Dallas to Austin Chauffeured SUVs</title>
<link rel="stylesheet" href="https://fonts.googleapis.com/css2?family=Archivo:wght@400;600;700&display=swap">
<style>
:root{
  --ink:#0a0a0a;
  --paper:#ffffff;
  --red:#e3262e;
  --stage:#8d8f94;
  --photo-gray-1:#9a9a9a;
  --photo-gray-2:#3a3a3a;
  --photo-warm-1:#d9d2c8;
  --photo-warm-2:#6b6b6b;
}
*{margin:0;padding:0;box-sizing:border-box}
html,body{width:911px;height:1200px;overflow:hidden}
body{background:var(--stage);font-family:"Archivo",Arial,sans-serif;color:var(--ink);position:relative}
.flyer{position:absolute;left:15px;top:31px;width:1265px;height:1635px;background:var(--paper);transform:scale(0.6957);transform-origin:0 0;overflow:hidden}
.hero{position:absolute;left:0;top:0;width:1265px;height:670px;background:var(--ink)}
.brand{position:absolute;left:0;top:0;width:660px;height:350px;display:flex;align-items:center;justify-content:center}
.brand-name{font-weight:600;font-size:86px;color:var(--paper);letter-spacing:2px}
.photo{position:absolute}
.photo-crew{left:660px;top:0;width:605px;height:400px;background:linear-gradient(160deg,var(--photo-gray-1),var(--photo-gray-2))}
.red-tab{position:absolute;top:633px;height:37px;background:var(--red)}
.red-tab.left{left:0;width:55px}
.red-tab.right{right:0;width:50px}
.photo-fleet{left:52px;top:350px;width:1163px;height:320px;border:7px solid var(--ink);border-bottom:none;border-radius:160px 160px 0 0/140px 140px 0 0;background:linear-gradient(180deg,var(--photo-warm-1) 0%,#bdb7ae 45%,var(--photo-warm-2) 100%)}
.photo-greeting{left:660px;top:670px;width:605px;height:387px;border-bottom-left-radius:330px 387px;background:linear-gradient(150deg,#c9c6c0,#3d3d3f 70%)}
.headline{position:absolute;left:65px;top:710px;font-weight:700;font-size:84px;line-height:76px;letter-spacing:-1.5px}
.features{position:absolute;top:1093px;list-style:none}
.features.left{left:65px;width:520px}
.features.right{left:662px;width:560px}
.features li{display:flex;gap:14px;font-size:22.5px;line-height:27px;margin-bottom:17px;min-height:54px}
.features li svg{flex:none;width:26px;height:26px;margin-top:2px}
.cta{position:absolute;left:0;top:1490px;width:640px;height:145px;background:var(--ink);border-top-right-radius:230px 145px;color:var(--paper);padding:30px 0 0 75px}
.cta-lead{font-size:24px}
.cta-url{font-size:42px;font-weight:700;margin-top:4px}
.base-bar{position:absolute;left:620px;top:1608px;width:645px;height:27px;background:var(--red)}
</style>
</head>
<body>
<svg width="0" height="0" style="position:absolute">
  <defs>
    <symbol id="tick" viewBox="0 0 26 26">
      <circle cx="12" cy="14" r="10" fill="none" stroke="#0a0a0a" stroke-width="2.4"/>
      <path d="M7 13.5l4.5 5L23 3" fill="none" stroke="#e3262e" stroke-width="3" stroke-linecap="round" stroke-linejoin="round"/>
    </symbol>
  </defs>
</svg>
<main class="flyer">
  <section class="hero">
    <div class="brand"><span class="brand-name">Marquel</span></div>
    <div class="photo photo-crew" role="img" aria-label="Row of uniformed chauffeurs in caps and dark suits, black and white"></div>
    <div class="red-tab left"></div>
    <div class="red-tab right"></div>
    <div class="photo photo-fleet" role="img" aria-label="Three SUVs in black, white and red with chauffeurs standing between them"></div>
  </section>

  <div class="photo photo-greeting" role="img" aria-label="Chauffeur helping a business traveler with luggage beside a black SUV"></div>

  <h1 class="headline">Dallas to<br>Austin<br>Chauffeured<br>SUVs</h1>

  <ul class="features left">
    <li><svg><use href="#tick"/></svg><span>Travel Dallas to Austin in a new 2025 Marlow Strider for $499 one-way</span></li>
    <li><svg><use href="#tick"/></svg><span>Trip includes a Uniformed Chauffeur who has a Commercial Drivers License (CDL)</span></li>
    <li><svg><use href="#tick"/></svg><span>You can Schedule Chauffeur Pickup at Your Home in Dallas</span></li>
    <li><svg><use href="#tick"/></svg><span>Our Chauffeur will Drop You Off at Your Final Destination in Austin</span></li>
    <li><svg><use href="#tick"/></svg><span>You can Schedule Chauffeur Return Pickup in Austin and Return Back to Dallas.</span></li>
  </ul>

  <ul class="features right">
    <li><svg><use href="#tick"/></svg><span>We offer Faster Times on Door-to-Door Travel than Bluecrest Airways</span></li>
    <li><svg><use href="#tick"/></svg><span>We offer Comparable Prices on Door-to-Door Travel Times than Bluecrest Airways</span></li>
    <li><svg><use href="#tick"/></svg><span>All of our trips are insured with $500k of commercial auto insurance</span></li>
    <li><svg><use href="#tick"/></svg><span>Our Passengers can Talk on Cell Phone &amp; Conduct Quill calls Throughout Travel</span></li>
    <li><svg><use href="#tick"/></svg><span>Our Passengers have Maximum Privacy, Comfort and First-Class Amenities.</span></li>
    <li><svg><use href="#tick"/></svg><span>Our Passengers Avoid Harwick Vale Field and KPR Airport hassles &amp; delays</span></li>
    <li><svg><use href="#tick"/></svg><span>Member Brenton Chamber of Commerce, Larkmoor Chamber of Commerce.</span></li>
  </ul>

  <footer class="cta">
    <p class="cta-lead">Book your trip today at</p>
    <p class="cta-url">www.ridemarquel.example</p>
  </footer>
  <div class="base-bar"></div>
</main>
</body>
</html>
```